Bildmark Speech for a trade show in Las Vegas

I've tried to create the powerpoint on my own. I used a template, but am not satisfied with the look and feel. I'd like something more professional looking. I need this powerpoint for an upcoming speech. I need the ppt to be in a format in which I can edit it for last-minute changes before my speech.

The Power Point has a lot of slides, but mostly I'm looking for a few good backgrounds so that every slide doesn't have to be completely unique. Plus, if you can clean up some of my graphics, that would be great too. Feel free to message me with any questions. Happy to help out.

Target Market(s)

Leaders in Construction and Manufacturing

Industry/Entity Type

Construction

Font styles to use
Sans Serif

Colors

Designer to choose colors to be used in the design.

Requirements
Must have
• The ability for me to edit the slides so that I can do some last-minute changes.
• I need to have the Bildmark/TerraMix logo (small round logo) on the bottom of each slide (or at least most of them).
Nice to have
• Pictures of people on construction sites using heavy equipment. (Backhoes, Loaders, Gravlers, Trench Falcon products, Ironmoth products, Harlan Voss products, etc)

```html
<!DOCTYPE html>
<html lang="en">
<head>
<meta charset="utf-8">
<title>Becoming a Construction Leader Worth Following – Slide Set</title>
<link href="https://fonts.googleapis.com/css2?family=Roboto+Condensed:ital,wght@0,300;0,400;0,700;1,300;1,400&display=swap" rel="stylesheet">
<style>
:root{
  --orange:#ef7a10;
  --orange-deep:#d9650a;
  --ink:#1c1c1c;
  --gray:#5f5f5f;
  --navy:#3d4d66;
  --sky-top:#b9dcf3;
  --sky-bottom:#eef7fd;
  --yellow:#f8d92c;
  --white:#ffffff;
}
*{box-sizing:border-box;margin:0;padding:0}
html,body{width:1200px;height:2201px;overflow:hidden;background:var(--white)}
body{font-family:"Roboto Condensed",Arial,sans-serif;color:var(--ink);position:relative}
.slide{position:absolute;width:439px;height:247px;overflow:hidden;background:var(--white);box-shadow:0 2px 6px rgba(0,0,0,.28)}
.col-l{left:89px}.col-r{left:672px}
.photo{position:absolute;inset:0}
.brand{position:absolute;right:6px;bottom:6px;display:flex;align-items:center;gap:3px;font-size:7px;font-weight:700;color:var(--navy);z-index:5}
.brand .dot{width:9px;height:9px;border-radius:50%;background:var(--orange)}
.on-dark .brand{color:var(--white)}
.abs{position:absolute}
/* slide 1 */
.welcome{left:205px;top:78px;font-size:40px;font-weight:700;color:var(--orange)}
/* slide 2 */
.title-stack{right:54px;top:100px;text-align:right;color:var(--white);font-weight:700;line-height:.95;text-shadow:0 1px 3px rgba(0,0,0,.4)}
.title-stack .sm{font-size:20px}.title-stack .lg{font-size:31px;font-weight:400}
/* slide 3 */
.invest{right:27px;top:85px;text-align:right;font-weight:700;line-height:.95}
.invest .sm{font-size:22px}.invest .lg{font-size:38px;color:var(--orange)}
/* slide 4 */
.ss-title{left:17px;top:43px;font-size:28px;color:var(--white);font-variant:small-caps}
.ss-q{left:17px;top:94px;width:270px;font-size:15px;font-style:italic;font-weight:300;color:var(--white);line-height:1.3}
/* lift */
.lift-title{left:16px;top:24px;font-size:21px;color:var(--orange);font-variant:small-caps}
.lift-sub{left:18px;top:48px;font-size:11px;letter-spacing:2.5px;color:var(--ink)}
/* mentor */
.mentor-title{left:0;right:0;top:16px;text-align:center;font-size:21px;color:var(--orange);font-variant:small-caps}
.mentor-note{left:32px;top:52px;width:136px;font-size:8px;font-weight:700;color:var(--orange);line-height:1.2}
.mentor-sub{left:32px;top:94px;width:60px;font-size:8px;color:var(--orange);line-height:1.2}
/* disciplines */
.disc-head{left:0;right:0;top:14px;text-align:center;font-size:10px;font-weight:700}
.disc-head b{font-size:15px;color:var(--orange)}
.dia{position:absolute;width:64px;height:64px;transform:rotate(45deg);box-shadow:2px 3px 5px rgba(0,0,0,.3);z-index:2}
.dia-text{position:absolute;width:76px;text-align:center;font-size:7px;color:var(--white);line-height:1.2;z-index:3}
.dia-centre{position:absolute;left:220px;top:132px;width:124px;height:124px;transform:translate(-50%,-50%) rotate(45deg);background:linear-gradient(135deg,#e9eef2,#9aa69b 60%,#6f6b55);box-shadow:2px 3px 6px rgba(0,0,0,.3);z-index:1}
.centre-label{left:180px;top:111px;width:80px;text-align:center;font-size:11px;font-weight:700;color:var(--orange);line-height:1.05;z-index:4}
/* capacity */
.disc-line{font-size:21px;font-weight:300}
.disc-line .k{color:var(--orange)}
.cap-q{left:0;right:0;top:178px;text-align:center;font-size:18px;font-weight:300;color:var(--white);line-height:1.3}
.cap-list{left:78px;top:74px;font-size:15px;font-weight:300;color:var(--white);line-height:1.32}
.cap-list ul{list-style:none;margin-left:54px}
.cap-list li::before{content:"• "}
.monkey-text{left:32px;top:22px}
.monkey-text .d{font-size:20px;font-weight:300;color:var(--orange)}
.monkey-text .t{font-size:20px;font-weight:400;margin-top:-2px}
.monkey-text .q{font-size:15px;color:var(--orange);margin-top:10px;line-height:1.2}
.monkey-text .m{font-size:10px;margin-top:12px;line-height:1}
.monkey-text .m p{margin-bottom:16px}
.frame{position:absolute;border:3px solid var(--orange)}
.callout{left:178px;top:143px;width:60px;height:44px;background:var(--orange);color:var(--white);font-size:10px;display:flex;align-items:center;justify-content:center;box-shadow:1px 2px 3px rgba(0,0,0,.3)}
</style>
</head>
<body>

<!-- Row 1 -->
<section class="slide col-l on-dark" style="top:26px">
  <div class="photo" role="img" aria-label="Excavator digging on a building site with a city skyline under a blue sky" style="background:linear-gradient(160deg,#5e8fc0 0%,#cfe0ef 45%,#c9a47a 80%,#7a5a3a 100%)"></div>
  <svg class="abs" style="left:0;top:0" width="439" height="247" viewBox="0 0 439 247">
    <polygon points="0,58 0,110 260,247 320,247" fill="#ef7a10" opacity=".55"/>
    <polygon points="439,85 439,160 300,247 230,247" fill="#ef7a10" opacity=".45"/>
  </svg>
  <div class="abs welcome">Welcome</div>
  <div class="brand"><span class="dot"></span>Bildmark</div>
</section>

<section class="slide col-r on-dark" style="top:26px">
  <div class="photo" role="img" aria-label="Two engineers in hard hats reviewing plans at a high-rise construction site with tower cranes" style="background:linear-gradient(180deg,#cfd2d4 0%,#a7aaa8 55%,#6f6a60 100%)"></div>
  <div class="abs title-stack"><div class="sm">BECOMING A</div><div class="lg">CONSTRUCTION LEADER</div><div class="sm">WORTH FOLLOWING</div></div>
  <div class="brand"><span class="dot"></span>Bildmark</div>
</section>

<!-- Row 2 -->
<section class="slide col-l" style="top:299px">
  <div class="photo" role="img" aria-label="Wall clock on a bright yellow background" style="background:radial-gradient(circle at 105px 120px,#f4f4f4 0 58px,#ffe86a 60px,#f6d21d 100%)"></div>
  <div class="abs invest"><div class="sm">YOUR</div><div class="lg">90-MINUTE</div><div class="sm">INVESTMENT</div></div>
  <div class="brand"><span class="dot"></span>Bildmark</div>
</section>

<section class="slide col-r on-dark" style="top:299px">
  <div class="photo" role="img" aria-label="Sprinter crouched at the start line on a running track" style="background:linear-gradient(120deg,#7d8388 0%,#9b9fa2 45%,#6c6a68 100%)"></div>
  <div class="abs ss-title">Starting &amp; Stopping</div>
  <div class="abs ss-q">In light of what you’ve just heard, what are some things you need to either <b>STOP</b> or <b>START</b> doing?</div>
  <div class="brand"><span class="dot"></span>Bildmark</div>
</section>

<!-- Row 3 -->
<section class="slide col-l" style="top:571px">
  <div class="photo" role="img" aria-label="Faded tower crane against a pale blue sky" style="background:linear-gradient(180deg,var(--sky-top),var(--sky-bottom))"></div>
  <div class="abs lift-title">Leaders Worth Following</div>
  <div class="abs lift-sub">THE LIFT EFFECT</div>
  <svg class="abs" style="left:0;top:0" width="439" height="247" viewBox="0 0 439 247">
    <defs><marker id="ah" markerWidth="6" markerHeight="6" refX="5" refY="3" orient="auto"><path d="M0,0 L6,3 L0,6 z" fill="#111"/></marker>
    <marker id="ar" markerWidth="6" markerHeight="6" refX="5" refY="3" orient="auto"><path d="M0,0 L6,3 L0,6 z" fill="#e01e25"/></marker></defs>
    <line x1="169" y1="212" x2="169" y2="54" stroke="#111" stroke-width="1.3" marker-end="url(#ah)"/>
    <line x1="169" y1="212" x2="388" y2="212" stroke="#111" stroke-width="1.3" marker-end="url(#ah)"/>
    <line x1="169" y1="212" x2="365" y2="57" stroke="#e01e25" stroke-width="1.3" marker-end="url(#ar)"/>
    <text x="0" y="0" font-size="8" font-family="Roboto Condensed, sans-serif" transform="translate(266,126) rotate(-38)">Size of your organization</text>
  </svg>
  <div class="brand"><span class="dot"></span>Bildmark</div>
</section>

<section class="slide col-r" style="top:571px">
  <div class="photo" role="img" aria-label="Faded tower crane against a pale blue sky" style="background:linear-gradient(180deg,var(--sky-top),var(--sky-bottom))"></div>
  <div class="abs lift-title">Leaders Worth Following</div>
  <div class="abs lift-sub">THE LIFT EFFECT</div>
  <svg class="abs" style="left:0;top:0" width="439" height="247" viewBox="0 0 439 247">
    <defs><marker id="ah2" markerWidth="6" markerHeight="6" refX="5" refY="3" orient="auto"><path d="M0,0 L6,3 L0,6 z" fill="#111"/></marker>
    <marker id="ag" markerWidth="6" markerHeight="6" refX="5" refY="3" orient="auto"><path d="M0,0 L6,3 L0,6 z" fill="#19a64a"/></marker>
    <marker id="ab" markerWidth="5" markerHeight="5" refX="2.5" refY="2.5" orient="auto"><path d="M0,0 L5,2.5 L0,5 z" fill="#1a2fd1"/></marker></defs>
    <line x1="169" y1="212" x2="169" y2="54" stroke="#111" stroke-width="1.3" marker-end="url(#ah2)"/>
    <line x1="169" y1="212" x2="388" y2="212" stroke="#111" stroke-width="1.3" marker-end="url(#ah2)"/>
    <polyline points="169,132 240,132 330,70" fill="none" stroke="#555" stroke-width="1.3"/>
    <line x1="169" y1="212" x2="365" y2="57" stroke="#19a64a" stroke-width="1.3" marker-end="url(#ag)"/>
    <g stroke="#1a2fd1" stroke-width="1.6">
      <line x1="250" y1="146" x2="250" y2="122" marker-end="url(#ab)"/>
      <line x1="262" y1="136" x2="262" y2="114" marker-end="url(#ab)"/>
      <line x1="274" y1="127" x2="274" y2="106" marker-end="url(#ab)"/>
      <line x1="286" y1="117" x2="286" y2="98" marker-end="url(#ab)"/>
      <line x1="298" y1="108" x2="298" y2="90" marker-end="url(#ab)"/>
      <line x1="310" y1="98" x2="310" y2="82" marker-end="url(#ab)"/>
      <line x1="322" y1="89" x2="322" y2="74" marker-end="url(#ab)"/>
      <line x1="334" y1="80" x2="334" y2="66" marker-end="url(#ab)"/>
    </g>
    <text font-size="7.5" font-family="Roboto Condensed, sans-serif" transform="translate(253,110) rotate(-38)">Your Leadership Skills</text>
  </svg>
  <div class="brand"><span class="dot"></span>Bildmark</div>
</section>

<!-- Row 4 -->
<section class="slide col-l" style="top:843px">
  <div class="abs mentor-title">What To Mentor?</div>
  <div class="abs mentor-note">Employees just doing their job will not get them a pay raise or a promotion.</div>
  <svg class="abs" style="left:0;top:0" width="439" height="247" viewBox="0 0 439 247">
    <g transform="translate(220,141) scale(1,.5)">
      <circle r="70" fill="none" stroke="#3b3b3b" stroke-width="80"/>
    </g>
    <g transform="translate(220,127) scale(1,.5)" fill="none" stroke-width="80">
      <circle r="70" stroke="#d96a0a" stroke-dasharray="55 385" stroke-dashoffset="110"/>
      <circle r="70" stroke="#c9c9c9" stroke-dasharray="55 385" stroke-dashoffset="55"/>
      <circle r="70" stroke="#9a9a9a" stroke-dasharray="55 385" stroke-dashoffset="0"/>
      <circle r="70" stroke="#7a7a7a" stroke-dasharray="55 385" stroke-dashoffset="-55"/>
      <circle r="70" stroke="#5a5a5a" stroke-dasharray="55 385" stroke-dashoffset="-110"/>
      <circle r="70" stroke="#454545" stroke-dasharray="55 385" stroke-dashoffset="-165"/>
      <circle r="70" stroke="#ee9a7c" stroke-dasharray="55 385" stroke-dashoffset="-220"/>
      <circle r="70" stroke="#e2e2e2" stroke-dasharray="55 385" stroke-dashoffset="-275"/>
      <circle r="30" fill="#fff" stroke="none"/>
    </g>
    <text x="220" y="130" text-anchor="middle" font-size="8" fill="#d96a0a" font-family="Roboto Condensed, sans-serif">Doing their job.</text>
  </svg>
  <div class="brand"><span class="dot"></span>Bildmark</div>
</section>

<section class="slide col-r" style="top:843px">
  <div class="abs mentor-title">What To Mentor?</div>
  <div class="abs mentor-note">Employees just doing their job will not get them a pay raise or a promotion.</div>
  <div class="abs mentor-sub">How they do their job <b>will.</b></div>
  <svg class="abs" style="left:0;top:0" width="439" height="247" viewBox="0 0 439 247">
    <g transform="translate(220,141) scale(1,.5)">
      <circle r="70" fill="none" stroke="#3b3b3b" stroke-width="80"/>
    </g>
    <g transform="translate(220,127) scale(1,.5)" fill="none" stroke-width="80">
      <circle r="70" stroke="#d96a0a" stroke-dasharray="55 385" stroke-dashoffset="110"/>
      <circle r="70" stroke="#c9c9c9" stroke-dasharray="55 385" stroke-dashoffset="55"/>
      <circle r="70" stroke="#9a9a9a" stroke-dasharray="55 385" stroke-dashoffset="0"/>
      <circle r="70" stroke="#7a7a7a" stroke-dasharray="55 385" stroke-dashoffset="-55"/>
      <circle r="70" stroke="#5a5a5a" stroke-dasharray="55 385" stroke-dashoffset="-110"/>
      <circle r="70" stroke="#454545" stroke-dasharray="55 385" stroke-dashoffset="-165"/>
      <circle r="70" stroke="#ee9a7c" stroke-dasharray="55 385" stroke-dashoffset="-220"/>
      <circle r="70" stroke="#e2e2e2" stroke-dasharray="55 385" stroke-dashoffset="-275"/>
      <circle r="30" fill="#fff" stroke="none"/>
    </g>
    <g font-size="7.5" fill="#fff" font-family="Roboto Condensed, sans-serif" text-anchor="middle">
      <text x="247" y="81">Driver</text>
      <text x="198" y="79">Teamwork</text>
      <text x="290" y="97">Collaboration</text>
      <text x="303" y="121">No Rumors</text>
      <text x="284" y="148">Low Stress</text>
      <text x="222" y="160">Appreciative</text>
      <text x="156" y="147">Thinking Ahead</text>
      <text x="146" y="116">Actively</text><text x="146" y="124">Engaged</text>
      <text x="155" y="97">No Whining</text>
    </g>
    <text x="220" y="123" text-anchor="middle" font-size="8" fill="#d96a0a" font-family="Roboto Condensed, sans-serif">You doing</text>
    <text x="220" y="133" text-anchor="middle" font-size="8" fill="#d96a0a" font-family="Roboto Condensed, sans-serif">your job.</text>
  </svg>
  <div class="brand"><span class="dot"></span>Bildmark</div>
</section>

<!-- Row 5 -->
<section class="slide col-l" style="top:1116px">
  <div class="abs disc-head">BECOMING A <b>CONSTRUCTION LEADER</b> WORTH FOLLOWING</div>
  <div class="dia-centre" role="img" aria-label="Worker in a hard hat overlooking a construction site"></div>
  <div class="dia" style="left:84px;top:54px;background:var(--orange)"></div>
  <div class="dia" style="left:293px;top:54px;background:var(--navy)"></div>
  <div class="dia" style="left:84px;top:151px;background:#9a9a9a"></div>
  <div class="dia" style="left:293px;top:151px;background:#6f757d"></div>
  <div class="abs centre-label">The<br>FOUR<br>Disciplines</div>
  <div class="dia-text" style="left:78px;top:78px">INCREASING YOUR CAPACITY</div>
  <div class="dia-text" style="left:287px;top:78px">DRIVING THE RIGHT CULTURE</div>
  <div class="dia-text" style="left:78px;top:175px">YOUR EMPLOYEES’ LEADERSHIP STYLE</div>
  <div class="dia-text" style="left:287px;top:175px">BEING A TRUST DRIVER</div>
  <div class="brand"><span class="dot"></span>Bildmark</div>
</section>

<section class="slide col-r on-dark" style="top:1116px">
  <div class="photo" role="img" aria-label="Close-up of a yellow loader cab and arm against a hazy sky" style="background:linear-gradient(90deg,#c9c9c4 0%,#7b7a72 45%,#3d3f42 100%)"></div>
  <div class="abs" style="left:0;right:0;bottom:0;height:6px;background:repeating-linear-gradient(45deg,#222 0 5px,var(--orange) 5px 10px)"></div>
  <div class="abs" style="left:29px;top:48px;width:126px;height:126px;transform:rotate(45deg);background:var(--orange)"></div>
  <div class="abs" style="left:12px;top:98px;width:160px;text-align:center;color:var(--white)">
    <div style="font-size:9px;font-weight:300">The Four Disciplines</div>
    <div style="font-size:17px;font-weight:300;line-height:1.25">1.INCREASING YOUR CAPACITY</div>
  </div>
  <div class="brand"><span class="dot"></span>Bildmark</div>
</section>

<!-- Row 6 -->
<section class="slide col-l on-dark" style="top:1387px">
  <div class="abs" role="img" aria-label="Skyline silhouette with tower cranes and an excavator" style="left:0;right:0;top:128px;bottom:0;background:var(--gray)"></div>
  <div class="abs disc-line" style="right:40px;top:34px"><span class="k">Discipline:</span>&nbsp; YOUR CAPACITY</div>
  <div class="abs cap-q">If you could increase your capacity, what<br>should you use this additional time to do?</div>
  <div class="brand"><span class="dot"></span>Bildmark</div>
</section>

<section class="slide col-r on-dark" style="top:1387px;background:linear-gradient(135deg,#d9650a,#f28a1e 60%,#ec7a12)">
  <div class="abs disc-line" style="right:40px;top:34px;color:var(--white)">Discipline:&nbsp; YOUR CAPACITY</div>
  <div class="abs cap-list">Increasing your capacity provides you with<br>additional time to:
    <ul><li>Be more strategic.</li><li>Serve your boss.</li><li>Serve your peers.</li><li>Do your job.</li><li>Serve EMPLOYEES.</li></ul>
  </div>
  <div class="brand"><span class="dot"></span>Bildmark</div>
</section>

<!-- Row 7 -->
<section class="slide col-l" style="top:1659px">
  <div class="abs monkey-text">
    <div class="d">Discipline:</div><div class="t">YOUR CAPACITY</div>
    <div class="q">When your employees talk to<br>you, what do they do?</div>
    <div class="m"><p>-Leave monkeys on your back?</p><p>-Add monkeys to your back?</p><p>-Take monkeys off your back?</p></div>
  </div>
  <div class="frame" style="left:272px;top:19px;width:125px;height:188px"></div>
  <div class="abs" role="img" aria-label="Office worker at a desk with a monkey on his back" style="left:251px;top:42px;width:124px;height:183px;background:linear-gradient(160deg,#b9b3a8,#6f6a5e 60%,#9b7b52)"></div>
  <div class="brand"><span class="dot"></span>Bildmark</div>
</section>

<section class="slide col-r" style="top:1659px">
  <div class="abs monkey-text">
    <div class="d">Discipline:</div><div class="t">YOUR CAPACITY</div>
    <div class="q">When your employees talk to<br>you, what do they do?</div>
    <div class="m"><p>-Leave monkeys on your back?</p><p>-Add monkeys to your back?</p><p>-Take monkeys off your back?</p></div>
  </div>
  <svg class="abs" style="left:0;top:0" width="439" height="247" viewBox="0 0 439 247"><polygon points="188,180 160,200 200,186" fill="#ef7a10"/></svg>
  <div class="abs callout">Their Goal</div>
  <div class="frame" style="left:272px;top:19px;width:125px;height:188px"></div>
  <div class="abs" role="img" aria-label="Office worker at a desk with a monkey on his back" style="left:251px;top:42px;width:124px;height:183px;background:linear-gradient(160deg,#b9b3a8,#6f6a5e 60%,#9b7b52)"></div>
  <div class="brand"><span class="dot"></span>Bildmark</div>
</section>

<!-- Row 8 -->
<section class="slide col-l" style="top:1932px">
  <div class="frame" style="left:21px;top:19px;width:125px;height:188px"></div>
  <div class="abs" role="img" aria-label="Crew in safety vests working beside red trenching equipment" style="left:43px;top:42px;width:124px;height:183px;background:linear-gradient(160deg,#6f9a4c,#9b3a2a 45%,#7a5a3e)"></div>
  <div class="abs" style="right:27px;top:30px;text-align:right">
    <div style="font-size:20px;font-weight:300;color:var(--orange)">Discipline:</div>
    <div style="font-size:20px">YOUR CAPACITY</div>
    <div style="font-size:39px;color:var(--orange);line-height:1.25;margin-top:10px">THE<br>WRENCH</div>
  </div>
  <div class="brand"><span class="dot"></span>Bildmark</div>
</section>

<section class="slide col-r on-dark" style="top:1932px">
  <div class="photo" role="img" aria-label="Silhouette of a businessman at an office window, orange tint" style="background:linear-gradient(90deg,#b8560c 0%,#d9701a 40%,#e48a30 100%)"></div>
  <div class="abs" style="right:27px;top:30px;text-align:right;color:var(--white)">
    <div style="font-size:20px;font-weight:300">Discipline:</div>
    <div style="font-size:20px">YOUR CAPACITY</div>
    <div style="font-size:15px;font-weight:700;margin-top:14px">Think Ahead of your boss.</div>
    <div style="font-size:15px;font-weight:300;margin-top:14px;line-height:1.3">What are some examples of how<br>you can “think ahead of your boss”?</div>
  </div>
  <div class="brand"><span class="dot"></span>Bildmark</div>
</section>

</body>
</html>
```